Youth deer hunt give away flyer.

We need a flyer designed for a youth deer hunt giveaway that we are doing. We are an Illinois whitetail deer hunting outfitter. We house and feed our clients as well as providing them with a guided deer hunt. It needs to include images as well as details about the giveaway. Im looking for a proffesional, looking flyer

Target Market(s)

rednecks, hunters

Industry/Entity Type

Hunting

Font styles to use
Serif
Sans Serif

Colors
000000
dbdbdb
ffffff
474747

Requirements
Must have
• not sure
Nice to have
• not sure
Should not have
• not sure

```html
<!DOCTYPE html>
<html lang="en">
<head>
<meta charset="utf-8">
<title>2018 Youth Firearm Hunt – Hollow Creek Outfitting</title>
<link href="https://fonts.googleapis.com/css2?family=Cinzel:wght@400;600&family=Lato:wght@400;700&display=swap" rel="stylesheet">
<style>
  :root{
    --black:#000000;
    --ink:#1f1f1f;
    --charcoal:#2a2a2a;
    --slate:#474747;
    --mist:#dbdbdb;
    --white:#ffffff;
    --page:#d6d6d6;
  }
  *{box-sizing:border-box;margin:0;padding:0}
  html,body{width:1200px;height:1200px;overflow:hidden}
  body{background:var(--page);font-family:'Lato',sans-serif;color:var(--ink);position:relative}
  .flyer{position:absolute;left:151px;top:18px;width:898px;height:1164px;background:var(--white)}
  .flyer-art{position:absolute;left:0;top:0}
  .abs{position:absolute}

  .brand-name{left:589px;top:262px;width:240px;text-align:center;font-family:'Cinzel',serif;font-weight:400;font-size:21px;line-height:26px;color:var(--white);letter-spacing:.5px}

  .title{left:78px;top:408px;font-family:'Cinzel',serif;color:var(--black)}
  .title-year{font-size:46px;font-weight:600;line-height:54px;letter-spacing:1px}
  .title-event{font-size:56px;font-weight:400;line-height:64px;color:#2e2e2e;letter-spacing:2px}

  .details{left:94px;top:552px;width:340px;list-style:none}
  .details li{position:relative;padding-left:22px;font-size:16px;line-height:19px;color:#222;margin-bottom:13px}
  .details li::before{content:"";position:absolute;left:0;top:7px;width:7px;height:7px;border-radius:50%;background:var(--black)}
  .details .date{font-weight:700;font-size:17px;margin-bottom:11px}

  .about{left:492px;top:592px;width:340px;color:var(--white)}
  .about h2{font-family:'Cinzel',serif;font-weight:400;font-size:16px;letter-spacing:1px;margin-bottom:8px}
  .about p{font-size:11.4px;line-height:13.6px;text-align:justify}

  .contact{left:367px;top:1000px;color:var(--white)}
  .contact h3{font-family:'Cinzel',serif;font-weight:400;font-size:17px;letter-spacing:1.2px;margin-bottom:6px}
  .contact ul{list-style:none}
  .contact li{display:flex;align-items:flex-start;gap:10px;font-size:13.5px;line-height:18.5px}
  .contact svg{flex:none;margin-top:4px}
</style>
</head>
<body>
<main class="flyer">
  <svg class="flyer-art" width="898" height="1164" viewBox="0 0 898 1164">
    <defs>
      <linearGradient id="paper" x1="0" y1="0" x2="0" y2="1">
        <stop offset="0" stop-color="#e6e6e6"/>
        <stop offset=".45" stop-color="#fafafa"/>
        <stop offset=".8" stop-color="#ececec"/>
        <stop offset="1" stop-color="#dedede"/>
      </linearGradient>
      <linearGradient id="cabinTone" x1="0" y1="0" x2="1" y2="1">
        <stop offset="0" stop-color="#8a4a22"/>
        <stop offset=".5" stop-color="#b0662f"/>
        <stop offset="1" stop-color="#6e3a1c"/>
      </linearGradient>
      <linearGradient id="swoosh" x1="0" y1="0" x2="1" y2="0">
        <stop offset="0" stop-color="#9a9a9a"/>
        <stop offset=".5" stop-color="#111"/>
        <stop offset="1" stop-color="#3a3a3a"/>
      </linearGradient>
      <linearGradient id="trophyTone" x1="0" y1="0" x2="0" y2="1">
        <stop offset="0" stop-color="#9b6a3e" stop-opacity="0"/>
        <stop offset=".25" stop-color="#8f5f36"/>
        <stop offset="1" stop-color="#5a3a22"/>
      </linearGradient>
      <linearGradient id="lodgeTone" x1="0" y1="0" x2="0" y2="1">
        <stop offset="0" stop-color="#c9cdd2"/>
        <stop offset=".5" stop-color="#b8823f"/>
        <stop offset="1" stop-color="#5f8a3a"/>
      </linearGradient>
      <linearGradient id="fieldTone" x1="0" y1="0" x2="1" y2="1">
        <stop offset="0" stop-color="#6b4a2a"/>
        <stop offset="1" stop-color="#a0743e"/>
      </linearGradient>
    </defs>

    <rect class="paper" x="20" y="19" width="858" height="1123" fill="url(#paper)"/>

    <path class="cabin-photo" role="img" aria-label="Photo of the log cabin interior with kitchen, mounted deer trophies and glass doors"
      d="M20,19 H878 V292 Q620 378 350 343 Q140 318 20 188 Z" fill="url(#cabinTone)"/>
    <path class="top-swoosh" d="M20,196 Q140 328 350 352 Q620 386 878 298 V318 Q620 420 350 378 Q128 346 20 232 Z" fill="url(#swoosh)"/>

    <circle cx="709" cy="275" r="131" fill="var(--white)"/>
    <circle class="brand-badge" cx="709" cy="275" r="122" fill="var(--charcoal)"/>

    <path class="about-panel" d="M478,580 L520,574 L600,578 L700,573 L790,579 L846,576 L842,620 L848,700 L843,780 L847,836 L780,839 L700,833 L610,840 L530,835 L474,839 L478,780 L472,700 L477,630 Z" fill="var(--charcoal)"/>

    <rect class="trophy-photo" role="img" aria-label="Photo of a young hunter in an orange cap with a harvested whitetail buck" x="20" y="770" width="400" height="372" fill="url(#trophyTone)"/>

    <path class="bottom-swoosh" d="M360,1005 Q480,952 620,946 L878,946 V960 L590,960 Q450,966 360,1005 Z" fill="#8a8a8a"/>
    <path class="contact-band" d="M262,1142 C320,1012 440,968 580,962 L878,964 V1142 Z" fill="var(--charcoal)"/>

    <circle cx="616" cy="964" r="76" fill="var(--white)"/>
    <circle class="lodge-photo" role="img" aria-label="Photo of the wooden guest cabin on a green lawn" cx="616" cy="964" r="70" fill="url(#lodgeTone)"/>
    <circle cx="750" cy="1019" r="71" fill="var(--white)"/>
    <circle class="field-photo" role="img" aria-label="Photo of a hunter with a buck in autumn woods" cx="750" cy="1019" r="65" fill="url(#fieldTone)"/>

    <line x1="566" y1="1097" x2="628" y2="1097" stroke="#9a9a9a" stroke-width="1"/>
    <circle class="social-dot" cx="643" cy="1096" r="11" fill="var(--white)"/>
    <circle class="social-dot" cx="676" cy="1096" r="11" fill="var(--white)"/>
  </svg>

  <div class="abs brand-name">Hollow Creek Outfitting</div>

  <h1 class="abs title">
    <div class="title-year">2018 Youth</div>
    <div class="title-event">Firearm Hunt</div>
  </h1>

  <ul class="abs details">
    <li class="date">October 6-8, 2018</li>
    <li>4 night stay in our private cabin that include meals for 2 parents and the child.</li>
    <li>Guided shotgun hunt on strictly managed properties.</li>
    <li>Ground blinds in place</li>
    <li>Permit and license fees are the hunters responsibility.</li>
  </ul>

  <section class="abs about">
    <h2>About us</h2>
    <p>Hollow Creek Outfitting is a family owned and operated deer hunting outfitter located in Morgan and Scott Counties in west central Illinois. We provide low pressure, trophy whitetail hunts on privately owned farms across the region. The Hardins are lifelong residents and hunters of Morgan County, with the family farm being established well over 150 years ago.<br>To go along with guiding deer and turkey hunters, we also offer a wide variety of professional hunting services that include whitetail land consulting, scouting services, CRP and food plot plantings and more.</p>
  </section>

  <section class="abs contact">
    <h3>Caleb Hardin</h3>
    <ul>
      <li><svg width="11" height="11" viewBox="0 0 12 12"><path d="M2.5 1 L4.5 1 L5.5 3.5 L4 4.6 Q5 7 7.4 8 L8.5 6.5 L11 7.5 V9.5 Q11 11 9.5 11 Q1 10 1 2.5 Q1 1 2.5 1Z" fill="#fff"/></svg>(217) 555-0148</li>
      <li><svg width="11" height="11" viewBox="0 0 12 12"><circle cx="6" cy="6" r="5" fill="none" stroke="#fff" stroke-width="1.3"/><path d="M1 6 H11 M6 1 Q3 6 6 11 Q9 6 6 1" fill="none" stroke="#fff" stroke-width="1"/></svg>www.hollowcreekoutfitting.com</li>
      <li><svg width="11" height="11" viewBox="0 0 12 12"><rect x="1" y="2.5" width="10" height="7" fill="none" stroke="#fff" stroke-width="1.3"/><path d="M1 3 L6 7 L11 3" fill="none" stroke="#fff" stroke-width="1.1"/></svg>hollowcreekoutfitting@mail.com</li>
      <li><svg width="11" height="12" viewBox="0 0 12 13"><path d="M6 12 Q1.5 6.5 1.5 4.5 A4.5 4.5 0 0 1 10.5 4.5 Q10.5 6.5 6 12Z" fill="#fff"/><circle cx="6" cy="4.5" r="1.6" fill="#2a2a2a"/></svg>1840 Timber Lane<br>Ashland, Illinois 62612</li>
    </ul>
  </section>
</main>
</body>
</html>
```